International Sex Coach needs a Book Cover in less than 3 days

I need a cover design for my book coming out next week titled "The Open Map of Desire". The book explores the origins of our cultural ideas about sexuality and taboo and is interwoven with personal memoir.
The reader must feel that they are being pulled into an intimate sexual story, but also a deeper understanding of sex itself. Like they are jumping into bed with me, you might say. I would like the title to take up the majority of the space over an image of 3D, very real bed sheets, but I am open to your ideas. I haven't purchased any images yet, but there are a few below I was drawn to.
In its essence, this book is designed to reeducate the reader about sexuality and open them up to a new paradigm of sexual wellness.
The author name is Marisa Tolven. Page must also include the phrase: a revolutionary new approach to sexuality, relationship and love.
Size 6" x 9" (15.24 x 22.86 cm)
Thanks!
Updates

Target Market(s)

Sexually active men and women.

Industry/Entity Type

Wellness

Font styles to use
Serif

```html
<!DOCTYPE html>
<html lang="en">
<head>
<meta charset="utf-8">
<title>The Open Map of Desire — Book Cover</title>
<link rel="stylesheet" href="https://fonts.googleapis.com/css2?family=Cormorant+Garamond:wght@400;500&display=swap">
<style>
  :root {
    --sheet-light: #f6f5f1;
    --sheet-shade: #d9d7d0;
    --panel-deep: #1f1816;
    --panel-warm: #64574a;
    --photo-hair: #d9a86a;
    --photo-skin: #efc4a6;
    --photo-shadow: #a8744c;
    --type-light: #ffffff;
    --type-soft: #e9e4dc;
  }
  html, body {
    margin: 0;
    padding: 0;
    width: 823px;
    height: 1200px;
    overflow: hidden;
    background: #ffffff;
  }
  .book-cover {
    position: relative;
    width: 823px;
    height: 1200px;
    overflow: hidden;
  }
  .book-cover__art {
    position: absolute;
    inset: 0;
    display: block;
  }
  .cover-text {
    font-family: "Cormorant Garamond", Georgia, serif;
    text-anchor: end;
  }
  .cover-title__line {
    fill: var(--type-light);
    font-weight: 500;
    letter-spacing: 1px;
  }
  .cover-title__line--first { font-size: 55px; }
  .cover-title__line--second { font-size: 84px; }
  .cover-tagline {
    fill: var(--type-soft);
    font-size: 33px;
    font-weight: 400;
    letter-spacing: 0.5px;
  }
  .cover-author {
    fill: var(--type-soft);
    font-size: 21px;
    font-weight: 400;
    letter-spacing: 0.5px;
  }
</style>
</head>
<body>
  <main class="book-cover">
    <svg class="book-cover__art" width="823" height="1200" viewBox="0 0 823 1200" xmlns="http://www.w3.org/2000/svg">
      <defs>
        <linearGradient id="sheet-tone" x1="0" y1="0" x2="1" y2="1">
          <stop offset="0" stop-color="var(--sheet-light)"/>
          <stop offset="0.5" stop-color="var(--sheet-shade)"/>
          <stop offset="1" stop-color="var(--sheet-light)"/>
        </linearGradient>
        <radialGradient id="panel-tone" cx="0.45" cy="0.5" r="0.75">
          <stop offset="0" stop-color="var(--panel-deep)"/>
          <stop offset="0.6" stop-color="#2e2420"/>
          <stop offset="1" stop-color="var(--panel-warm)"/>
        </radialGradient>
        <linearGradient id="photo-tone" x1="0" y1="0" x2="1" y2="1">
          <stop offset="0" stop-color="var(--photo-hair)"/>
          <stop offset="0.45" stop-color="var(--photo-skin)"/>
          <stop offset="1" stop-color="var(--photo-shadow)"/>
        </linearGradient>
      </defs>

      <rect class="cover-sheets" width="823" height="1200" fill="url(#sheet-tone)"
            role="img" aria-label="Photograph of soft white satin bed sheets"/>

      <polygon class="cover-panel" points="689,0 823,0 823,1200 689,1200 -279,600"
               fill="url(#panel-tone)"/>

      <polygon class="cover-portrait" points="0,160 743,608 0,1058"
               fill="url(#photo-tone)"
               role="img" aria-label="Photograph of a blonde woman with eyes lowered, lying on the sheets"/>

      <g class="cover-text">
        <text class="cover-title__line cover-title__line--first" x="785" y="308">THE OPEN MAP</text>
        <text class="cover-title__line cover-title__line--second" x="785" y="384">OF DESIRE</text>

        <text class="cover-tagline" x="780" y="831">A revolutionary</text>
        <text class="cover-tagline" x="780" y="873">new approach</text>
        <text class="cover-tagline" x="780" y="915">to sexuality,</text>
        <text class="cover-tagline" x="780" y="957">relationship and love.</text>

        <text class="cover-author" x="767" y="1011">Marisa Tolven</text>
      </g>
    </svg>
  </main>
</body>
</html>
```